Lumora Assist overview brochure

Take the word document that is attached and turn it into a brochure. (Thinking one page, front and back.) the only existing branding/colors we have is the logo that is on the document. It may require a phone all or a bit of back and forth in text to explain some of the concepts in the attached document.

Target Market(s)

Call centers

Industry/Entity Type

It Service

Font styles to use
Sans Serif

Colors

Designer to choose colors to be used in the design.

Requirements
Must have
• A crisp professional look

```html
<!DOCTYPE html>
<html lang="en">
<head>
<meta charset="utf-8">
<title>Lumora Assist overview brochure</title>
<link rel="stylesheet" href="https://fonts.googleapis.com/css2?family=Raleway:wght@300;400;500;600;700;800&display=swap">
<style>
:root{
  --stage:#a3a3a3;
  --paper:#ffffff;
  --blue:#2aa1e0;
  --blue-deep:#1f8fd0;
  --ink:#2b2b2b;
  --body:#4a4a4a;
  --charcoal:#3a3a3c;
  --charcoal-dark:#2a2a2c;
  --hero-grey:#e3e3e3;
}
*{box-sizing:border-box;margin:0;padding:0}
html,body{width:1200px;height:1200px;overflow:hidden}
body{background:var(--stage);font-family:'Raleway',sans-serif;position:relative;color:var(--body)}
.page{position:absolute;top:263px;width:520px;height:673px;background:var(--paper);overflow:hidden;box-shadow:0 6px 18px rgba(0,0,0,.25)}
.page--front{left:78px}
.page--back{left:602px}
.abs{position:absolute}

/* front header */
.brand{position:absolute;left:296px;top:30px;display:flex;align-items:center;gap:10px}
.brand__dot{width:34px;height:34px;border-radius:50%;background:var(--blue)}
.brand__name{font-size:22px;font-weight:600;color:var(--blue);letter-spacing:.5px;line-height:1.05;text-transform:uppercase;width:170px}
.hero{position:absolute;left:0;top:93px;width:520px;height:236px;background:linear-gradient(90deg,#f4f4f4 0%,var(--hero-grey) 50%,#bdbdbd 100%)}
.hero__bar{position:absolute;left:31px;top:56px;width:5px;height:144px;background:var(--blue)}
.hero__headline{position:absolute;left:45px;top:56px;font-size:18.6px;line-height:19.2px;font-weight:500;color:var(--ink);text-transform:uppercase}
.hero__headline b{color:var(--blue-deep);font-weight:800}
.hero__art{position:absolute;left:272px;top:14px;width:228px;height:222px;border-radius:50% 50% 0 40%;background:radial-gradient(circle at 45% 45%,#5fb8e6 0%,#9aa3aa 45%,rgba(190,190,190,0) 72%)}

.costs{position:absolute;left:0;top:329px;width:520px;height:101px;background:var(--blue)}
.costs__tab{position:absolute;left:148px;top:0;width:228px;height:20px;background:var(--charcoal);clip-path:polygon(0 0,100% 0,94% 100%,6% 100%);color:#fff;font-size:10px;font-weight:600;text-align:center;line-height:20px}
.cost{position:absolute;top:28px;display:flex;gap:10px;align-items:flex-start}
.cost__icon{width:50px;height:50px;border-radius:50%;background:#fff;display:flex;align-items:center;justify-content:center;flex:none}
.cost__text{color:#fff;font-size:10px;line-height:12.3px;font-weight:400;width:86px;margin-top:4px}
.costs__note{position:absolute;left:0;right:0;top:89px;text-align:center;font-size:7.5px;color:#1d3a4d}

.copy{position:absolute;top:451px;width:216px;font-size:10.2px;line-height:13.2px;text-align:justify;font-weight:400}
.copy p+p{margin-top:13px}

.footer{position:absolute;left:0;bottom:0;width:520px;height:36px;background:var(--charcoal);border-top:3px solid #5b5b5d;display:flex;justify-content:center;align-items:center;gap:30px;color:#fff;font-size:11.6px}
.footer::before{content:"";position:absolute;left:0;top:-3px;width:65%;height:3px;background:var(--blue)}
.footer span{display:flex;align-items:center;gap:6px}

/* back */
.stage-dark{position:absolute;left:0;top:0;width:520px;height:285px;background:linear-gradient(160deg,#55565a 0%,#3b3c3f 40%,#28292b 100%)}
.stage-dark::after{content:"";position:absolute;left:240px;right:0;bottom:0;height:4px;background:var(--blue)}
.title{position:absolute;left:31px;top:120px;color:#fff}
.title__small{font-size:27px;font-weight:300;letter-spacing:.5px;line-height:1}
.title__big{font-size:50px;font-weight:800;color:var(--blue);line-height:1;margin-top:6px;letter-spacing:.5px}
.scene-art{position:absolute;left:225px;top:12px;width:290px;height:270px;border-radius:18px;background:radial-gradient(circle at 55% 50%,#f2f2f2 0%,#cfd3d6 28%,#4a4b4f 60%,rgba(40,40,42,0) 75%)}

.section{position:absolute;font-size:10px;line-height:13.2px;color:var(--body)}
.section h3{font-size:15.5px;font-weight:500;color:var(--blue);text-transform:uppercase;line-height:16px}
.section ul{list-style:none;margin-top:1px}
.section li{position:relative;padding-left:18px}
.section li::before{content:"•";position:absolute;left:3px;font-size:8px}
.section__icon{position:absolute}
</style>
</head>
<body>

<section class="page page--front">
  <div class="brand">
    <div class="brand__dot"></div>
    <div class="brand__name">Lumora Assist</div>
  </div>

  <div class="hero">
    <div class="hero__bar"></div>
    <h1 class="hero__headline"><b>Lumora Assist</b><br><b>helps</b> contact centers<br>serve new customer<br>access channels,<br>improve customer<br>service, and lower<br>costs of <b>operation</b></h1>
    <div class="hero__art" role="img" aria-label="Illustration of communication icons bursting from a megaphone"></div>
  </div>

  <div class="costs">
    <div class="costs__tab">Existing channels have different costs</div>
    <div class="cost" style="left:31px">
      <div class="cost__icon"><svg width="28" height="28" viewBox="0 0 24 24" fill="#333"><path d="M6.6 10.8a15 15 0 0 0 6.6 6.6l2.2-2.2c.3-.3.7-.4 1-.2 1.1.4 2.3.6 3.6.6.6 0 1 .4 1 1V20c0 .6-.4 1-1 1A17 17 0 0 1 3 4c0-.6.4-1 1-1h3.5c.6 0 1 .4 1 1 0 1.2.2 2.4.6 3.6.1.3 0 .7-.2 1z"/></svg></div>
      <div class="cost__text">Telephone call with a live agent Average cost per call is $17*</div>
    </div>
    <div class="cost" style="left:194px">
      <div class="cost__icon"><svg width="30" height="24" viewBox="0 0 30 24" fill="none" stroke="#333" stroke-width="1.6"><rect x="2" y="4" width="26" height="18"/><path d="M2 4l13 10L28 4M2 22l10-9M28 22l-10-9"/></svg></div>
      <div class="cost__text">Email with a live agent Average cost per email is $15*</div>
    </div>
    <div class="cost" style="left:348px">
      <div class="cost__icon"><svg width="30" height="26" viewBox="0 0 30 26" fill="#333"><ellipse cx="12" cy="10" rx="11" ry="8"/><path d="M5 16l-2 6 7-4z"/><ellipse cx="20" cy="15" rx="8" ry="6" fill="#555"/><circle cx="8" cy="10" r="1.3" fill="#fff"/><circle cx="12" cy="10" r="1.3" fill="#fff"/><circle cx="16" cy="10" r="1.3" fill="#fff"/></svg></div>
      <div class="cost__text" style="width:92px">Webchat with a live agent Average cost per web chat is $12*</div>
    </div>
    <div class="costs__note">*Above costs are sited from an CSRI research paper</div>
  </div>

  <div class="copy" style="left:31px;top:447px">
    <p>The huge popularity of social media and messaging is creating customer preferences to communicate with your company using SMS text messaging, Chatwave Messenger, Teamloop, Vocal, Homely Voice, Nestly Hub, and many other new channels.</p>
    <p>App fatigue has set in. Customers are weary of installing, updating and learning how to use mobile apps. Your customers want to communicate with you using their messaging service of choice or just talk into their smart phone, computer, Homely Voice or similar device.</p>
  </div>
  <div class="copy" style="left:274px;top:447px">
    <p>Sensible automation of customer interactions on these new channels can provide better service at even lower costs of operation.</p>
    <p>According to Corvant's report, by 2020, 85% of customer interactions will be managed without a human.</p>
    <p>Using specific techniques, Lumora Assist will help you shift some traffic from higher cost telephone calls to lower cost messaging channels. Shaping your traffic into lower cost channels has great financial benefits.</p>
  </div>

  <footer class="footer">
    <span><svg width="12" height="12" viewBox="0 0 12 12" fill="none" stroke="#fff"><circle cx="6" cy="6" r="5"/><path d="M1 6h10M6 1c2 2 2 8 0 10M6 1c-2 2-2 8 0 10"/></svg>www.lumoraassist.net</span>
    <span><svg width="12" height="12" viewBox="0 0 12 12" fill="none" stroke="#fff"><circle cx="6" cy="6" r="5.3"/><path d="M4 3.5l1 1.5-.6.8a4 4 0 0 0 1.8 1.8l.8-.6 1.5 1-.6 1C6 9 3 6 3.5 4.1z" fill="#fff"/></svg>555-014-2290</span>
  </footer>
</section>

<section class="page page--back">
  <div class="stage-dark">
    <div class="scene-art" role="img" aria-label="Photo of a hand tapping a smartphone surrounded by messaging app speech bubbles"></div>
    <div class="title">
      <div class="title__small">ENGAGEMENT</div>
      <div class="title__big">MODEL</div>
    </div>
  </div>

  <svg class="section__icon" style="left:30px;top:304px" width="40" height="40" viewBox="0 0 40 40" fill="none" stroke="#2aa1e0" stroke-width="2"><path d="M16 6a10 10 0 0 0-6 18v5h12v-5a10 10 0 0 0-6-18z"/><path d="M12 32h8M13 35h6"/><rect x="24" y="16" width="12" height="16"/><path d="M27 21h6M27 25h6M27 29h4"/><path d="M4 8l3 3M2 16h4M28 4l-3 3"/></svg>
  <div class="section" style="left:76px;top:302px;width:180px">
    <h3>Proposal</h3>
    <p>Lumora Assist provides a written proposal. The proposal will describe our engagement methodologies and costs.</p>
  </div>

  <svg class="section__icon" style="left:30px;top:385px" width="40" height="40" viewBox="0 0 40 40" fill="none" stroke="#2aa1e0" stroke-width="2.2"><circle cx="22" cy="15" r="12"/><path d="M17 11h10M17 15h10M17 19h7"/><path d="M12 10a12 12 0 0 0 0 20l-2 6 6-4"/></svg>
  <div class="section" style="left:75px;top:387px;width:185px">
    <h3>Engagement</h3>
    <p>Lumora Assist will meet with all the relevant stake holders on site and gather information to identify:</p>
    <ul>
      <li>Historical traffic patterns.</li>
      <li>Actual costs by channel</li>
      <li>Review marketing plans that may impact customer service</li>
      <li>Review product plans that may impact customer service.</li>
      <li>Explore competition landscape as it relates to customer service.</li>
      <li>Review the existing corporate data store, analytics and reporting</li>
      <li>Review the current plans, metrics and budgets for customer service support</li>
    </ul>
  </div>

  <svg class="section__icon" style="left:270px;top:302px" width="36" height="42" viewBox="0 0 36 42" fill="none" stroke="#2aa1e0" stroke-width="2"><path d="M4 2h28v38H4z"/><path d="M9 14v10M14 10v14M19 16v8M24 12v12M9 28h18M9 33h14"/></svg>
  <div class="section" style="left:312px;top:302px;width:185px">
    <h3>Transformation<br>Report</h3>
    <ul style="margin-top:3px">
      <li>Executive summary</li>
      <li>Cost analysis per contact by channel</li>
      <li>Traffic patterns by channel</li>
      <li>Probable impacts of product and marketing plans</li>
      <li>Recommendations for achieving competitive advantage through service</li>
      <li>Recommendations for new channel types</li>
      <li>Recommendations for traffic shaping</li>
      <li>Near and long-term options for sensible automation</li>
      <li>Technology recommendations for implementing new channels</li>
      <li>Projected financial impact of recommendations</li>
    </ul>
  </div>

  <footer class="footer">
    <span><svg width="12" height="12" viewBox="0 0 12 12" fill="none" stroke="#fff"><circle cx="6" cy="6" r="5"/><path d="M1 6h10M6 1c2 2 2 8 0 10M6 1c-2 2-2 8 0 10"/></svg>www.lumoraassist.net</span>
    <span><svg width="12" height="12" viewBox="0 0 12 12" fill="none" stroke="#fff"><circle cx="6" cy="6" r="5.3"/><path d="M4 3.5l1 1.5-.6.8a4 4 0 0 0 1.8 1.8l.8-.6 1.5 1-.6 1C6 9 3 6 3.5 4.1z" fill="#fff"/></svg>555-014-2290</span>
  </footer>
</section>

</body>
</html>
```